Fenmoor Business Card

I want a business card for me and my employees.
On one side it must be in Greek and on the other side in English. The color must much the one of the logo

Target Market(s)

Customers that are looking for security and antipiracy advisors

Contact Information for Business Card

Title, Email, Phone, website , Mobile Address Zip code, city and country

Requirements
Must have
• The colors of our logo (the blue ones)

```html
<!DOCTYPE html>
<html lang="en">
<head>
<meta charset="utf-8">
<title>Fenmoor Advisory Business Cards</title>
<link href="https://fonts.googleapis.com/css2?family=Montserrat:wght@400;500;700&display=swap" rel="stylesheet">
<style>
  :root {
    --navy: #29226e;
    --navy-deep: #221c5e;
    --paper: #ffffff;
    --ink-light: #ffffff;
    --backdrop: #3b3b3d;
    --divider: rgba(255,255,255,0.45);
  }
  * { margin: 0; padding: 0; box-sizing: border-box; }
  html, body { width: 1200px; height: 1200px; overflow: hidden; }
  body {
    background: var(--backdrop);
    font-family: "Montserrat", sans-serif;
    display: flex;
    flex-direction: column;
    align-items: center;
    justify-content: center;
    gap: 56px;
  }
  .card {
    position: relative;
    width: 900px;
    height: 514px;
    border-radius: 40px;
    overflow: hidden;
    background: var(--paper);
    box-shadow: 0 18px 40px rgba(0,0,0,0.45);
  }
  .brand {
    position: absolute;
    top: 0; left: 0; right: 0;
    height: 196px;
    display: flex;
    align-items: center;
    justify-content: center;
    gap: 18px;
  }
  .brand-square {
    width: 52px; height: 52px;
    background: var(--navy);
  }
  .brand-name {
    font-weight: 700;
    font-size: 52px;
    letter-spacing: 2px;
    color: var(--navy);
    text-transform: uppercase;
    line-height: 1;
  }
  .rule {
    position: absolute;
    left: 0; right: 0;
    top: 200px;
    height: 6px;
    background: var(--navy);
  }
  .band {
    position: absolute;
    left: 0; right: 0; bottom: 0;
    top: 218px;
    background: linear-gradient(180deg, var(--navy) 0%, var(--navy-deep) 100%);
    color: var(--ink-light);
  }
  .person {
    position: absolute;
    left: 80px;
    bottom: 70px;
    font-size: 30px;
    line-height: 1.1;
    text-transform: uppercase;
  }
  .person .name { font-weight: 500; }
  .person .title { font-weight: 400; }
  .card--en .person .name, .card--en .person .title { font-weight: 700; }
  .split {
    position: absolute;
    left: 440px;
    top: 40px;
    width: 1.5px;
    height: 190px;
    background: var(--divider);
  }
  .contacts {
    position: absolute;
    left: 480px;
    top: 34px;
    list-style: none;
    font-size: 21px;
    line-height: 1.25;
  }
  .contacts li {
    display: flex;
    align-items: flex-start;
    gap: 12px;
    margin-bottom: 6px;
  }
  .contacts svg {
    flex: none;
    width: 22px; height: 22px;
    margin-top: 2px;
    fill: var(--ink-light);
  }
</style>
</head>
<body>

<section class="card card--el" lang="el">
  <div class="brand">
    <span class="brand-square"></span>
    <span class="brand-name">Fenmoor Advisory</span>
  </div>
  <div class="rule"></div>
  <div class="band">
    <div class="person">
      <div class="name">Πληρες Ονομα</div>
      <div class="title">Τιτλος</div>
    </div>
    <div class="split"></div>
    <ul class="contacts">
      <li><svg viewBox="0 0 24 24"><path d="M6.6 10.8a15 15 0 0 0 6.6 6.6l2.2-2.2a1 1 0 0 1 1-.25 11.4 11.4 0 0 0 3.6.57 1 1 0 0 1 1 1V20a1 1 0 0 1-1 1A17 17 0 0 1 3 4a1 1 0 0 1 1-1h3.5a1 1 0 0 1 1 1c0 1.25.2 2.45.57 3.57a1 1 0 0 1-.25 1z"/></svg>(000) 000 0000</li>
      <li><svg viewBox="0 0 24 24"><path d="M2 5h20v14H2zm2 2v.4l8 5.6 8-5.6V7zm0 2.8V17h16V9.8l-8 5.6z"/></svg>email@company.com</li>
      <li><svg viewBox="0 0 24 24"><path d="M12 2a10 10 0 1 0 0 20 10 10 0 0 0 0-20zm6.9 6h-2.9a15 15 0 0 0-1.4-3.9A8 8 0 0 1 18.9 8zM12 4a13 13 0 0 1 1.9 4h-3.8A13 13 0 0 1 12 4zM4.3 14a8 8 0 0 1 0-4h3.4a16 16 0 0 0 0 4zm.8 2h2.9a15 15 0 0 0 1.4 3.9A8 8 0 0 1 5.1 16zM8 8H5.1a8 8 0 0 1 4.3-3.9A15 15 0 0 0 8 8zm4 12a13 13 0 0 1-1.9-4h3.8A13 13 0 0 1 12 20zm2.3-6H9.7a14 14 0 0 1 0-4h4.6a14 14 0 0 1 0 4zm.3 5.9a15 15 0 0 0 1.4-3.9h2.9a8 8 0 0 1-4.3 3.9zm1.7-5.9a16 16 0 0 0 0-4h3.4a8 8 0 0 1 0 4z"/></svg>www.company.com</li>
      <li><svg viewBox="0 0 24 24"><path d="M12 2a7 7 0 0 0-7 7c0 5.2 7 13 7 13s7-7.8 7-13a7 7 0 0 0-7-7zm0 9.5A2.5 2.5 0 1 1 12 6.5a2.5 2.5 0 0 1 0 5z"/></svg><span>Οδός 123, 000<br>Η πόλη σας, 00000-000</span></li>
    </ul>
  </div>
</section>

<section class="card card--en" lang="en">
  <div class="brand">
    <span class="brand-square"></span>
    <span class="brand-name">Fenmoor Advisory</span>
  </div>
  <div class="rule"></div>
  <div class="band">
    <div class="person">
      <div class="name">Full Name</div>
      <div class="title">Title</div>
    </div>
    <div class="split"></div>
    <ul class="contacts">
      <li><svg viewBox="0 0 24 24"><path d="M6.6 10.8a15 15 0 0 0 6.6 6.6l2.2-2.2a1 1 0 0 1 1-.25 11.4 11.4 0 0 0 3.6.57 1 1 0 0 1 1 1V20a1 1 0 0 1-1 1A17 17 0 0 1 3 4a1 1 0 0 1 1-1h3.5a1 1 0 0 1 1 1c0 1.25.2 2.45.57 3.57a1 1 0 0 1-.25 1z"/></svg>(000) 000 0000</li>
      <li><svg viewBox="0 0 24 24"><path d="M2 5h20v14H2zm2 2v.4l8 5.6 8-5.6V7zm0 2.8V17h16V9.8l-8 5.6z"/></svg>email@company.com</li>
      <li><svg viewBox="0 0 24 24"><path d="M12 2a10 10 0 1 0 0 20 10 10 0 0 0 0-20zm6.9 6h-2.9a15 15 0 0 0-1.4-3.9A8 8 0 0 1 18.9 8zM12 4a13 13 0 0 1 1.9 4h-3.8A13 13 0 0 1 12 4zM4.3 14a8 8 0 0 1 0-4h3.4a16 16 0 0 0 0 4zm.8 2h2.9a15 15 0 0 0 1.4 3.9A8 8 0 0 1 5.1 16zM8 8H5.1a8 8 0 0 1 4.3-3.9A15 15 0 0 0 8 8zm4 12a13 13 0 0 1-1.9-4h3.8A13 13 0 0 1 12 20zm2.3-6H9.7a14 14 0 0 1 0-4h4.6a14 14 0 0 1 0 4zm.3 5.9a15 15 0 0 0 1.4-3.9h2.9a8 8 0 0 1-4.3 3.9zm1.7-5.9a16 16 0 0 0 0-4h3.4a8 8 0 0 1 0 4z"/></svg>www.company.com</li>
      <li><svg viewBox="0 0 24 24"><path d="M12 2a7 7 0 0 0-7 7c0 5.2 7 13 7 13s7-7.8 7-13a7 7 0 0 0-7-7zm0 9.5A2.5 2.5 0 1 1 12 6.5a2.5 2.5 0 0 1 0 5z"/></svg><span>123 Name Street, 000<br>Your City, 00000-000</span></li>
    </ul>
  </div>
</section>

</body>
</html>
```